Holiday Rental Leaflet

Want a DL size double sided leaflet to distribute via local businesses, markets, family and friends
HOLIDAY RENTALCarrickalinga - 17 Brindle Street Sleeps 8-10 (2 Queen, 1 Double, 2 bunks), 4 bedrooms, BIR to all bedrooms 2 Bathrooms, one with bath, 2 toilets Open Plan Lounge/Dining/Kitchen area Dining Table for 8 peopleReverse cycle airconditionerSlow combustion wood heaterTV/DVD, CD/RadioKitchen has m/wave, oven, fridge/freezer, dishwasherBBQ providedTimber decking with 2 outside tables and 12 chairs Washing Machine and dryer provided One street back from beach Smoke free zone No Pets
For further information or to book contact Joan on 0491 287 306 or email joanfarrow27@velmarnet.com.au

Industry/Entity Type

Kitchen

Requirements
Nice to have
• Have sent a variety of photos of the house. No need to use all of them, pick out the most relevant for the leaflet.

```html
<!DOCTYPE html>
<html lang="en">
<head>
<meta charset="utf-8">
<title>Holiday Rental Leaflet – Carrickalinga</title>
<link href="https://fonts.googleapis.com/css2?family=Crimson+Text:wght@400;700&family=Roboto+Condensed:wght@300;400&display=swap" rel="stylesheet">
<style>
:root{
  --teal:#4fa58f;
  --teal-dark:#2f7f6a;
  --sand:#f3d592;
  --ink:#555;
  --paper:#fff;
  --backdrop:#e8e6e2;
}
*{box-sizing:border-box;margin:0;padding:0}
html,body{width:1087px;height:1200px;overflow:hidden;background:var(--backdrop)}
body{position:relative;font-family:"Roboto Condensed",sans-serif;color:var(--ink)}
.leaflet{position:absolute;width:452px;height:950px;background:var(--paper);overflow:hidden;box-shadow:0 4px 14px rgba(0,0,0,.25)}
.leaflet--front{left:48px;top:80px}
.leaflet--back{left:569px;top:175px;height:948px}
.photo{position:absolute;left:0;width:100%}
.wave{position:absolute;left:0;width:100%;display:block}
.badge{position:absolute;left:0;top:38px;width:232px;height:64px;background:var(--teal);color:#fff;display:flex;align-items:center;padding-left:14px;gap:12px}
.badge__text{font-size:19px;line-height:22px;letter-spacing:.3px;text-align:center}
.badge__text span{display:block;border-bottom:1px solid #fff;padding-bottom:1px}
.badge__text span+span{font-size:21px}
.title{position:absolute;left:0;width:100%;text-align:center;font-family:"Crimson Text",serif;font-weight:700;font-size:27.5px;color:var(--teal-dark)}
.subtitle{position:absolute;left:0;width:100%;text-align:center;font-family:"Crimson Text",serif;font-size:22px;color:var(--ink);letter-spacing:.3px}
.section-rule{position:absolute;left:15px;right:15px;top:496px;display:flex;align-items:center;gap:14px;font-family:"Crimson Text",serif;font-size:14px;color:#aaa;letter-spacing:.5px}
.section-rule::before,.section-rule::after{content:"";flex:1;height:1px;background:#ccc}
.thumbs{position:absolute;left:15px;top:520px;display:flex;gap:10px}
.thumb{width:134px;height:113px;border:1px solid #ddd}
.features{position:absolute;list-style:none;font-weight:300}
.features li{position:relative;padding-left:19px;line-height:18px}
.features li::before{content:"›";position:absolute;left:0;top:3px;width:12px;height:12px;border-radius:50%;background:var(--sand);color:#fff;font-size:12px;line-height:11px;text-align:center;font-weight:400}
.features--front{font-size:15px;top:671px}
.features--front li{margin-bottom:4px}
.features--front.col-a{left:21px;width:210px}
.features--front.col-b{left:241px;width:205px}
.features--front .fit{font-size:14px}
.features--back{font-size:14px;top:492px}
.features--back li{margin-bottom:9px}
.features--back.col-a{left:22px;width:196px}
.features--back.col-b{left:219px;width:228px}
.nowrap{white-space:nowrap}
.tagline{position:absolute;left:0;width:100%;text-align:center;font-size:19px;font-weight:300;color:var(--ink)}
.contact-rule{position:absolute;left:0;width:100%;height:4px;background:var(--teal)}
.contact{position:absolute;left:0;bottom:0;width:100%;background:var(--teal);color:#fff;text-align:center}
.contact__lead{font-size:14.5px;margin-top:14px}
.contact__phone{font-size:22px;margin-top:2px;display:flex;justify-content:center;align-items:center;gap:8px;letter-spacing:.5px}
.contact__email{font-size:14px;margin-top:2px}
</style>
</head>
<body>

<section class="leaflet leaflet--front">
  <div class="photo" style="top:0;height:380px;background:linear-gradient(180deg,#c7d3d6 0%,#8f8a7e 30%,#6b5a44 55%,#4a4a42 75%,#a39d83 100%)" role="img" aria-label="Photo of the two-storey timber beach house with veranda and carport"></div>
  <svg class="wave" style="top:300px" height="110" viewBox="0 0 452 110" preserveAspectRatio="none" aria-hidden="true">
    <path d="M0,55 C120,125 270,100 452,35 L452,110 L0,110 Z" fill="#fff"/>
    <path d="M0,22 C90,95 240,98 452,22 L452,34 C270,100 120,122 0,55 Z" fill="var(--teal)"/>
    <path d="M150,88 C270,78 370,35 452,18 L452,30 C370,50 280,82 150,88 Z" fill="var(--sand)"/>
  </svg>
  <div class="badge">
    <svg width="30" height="26" viewBox="0 0 30 26" aria-hidden="true"><path d="M15 2 L29 14 L25 14 L25 25 L18 25 L18 17 L12 17 L12 25 L5 25 L5 14 L1 14 Z" fill="#fff"/></svg>
    <div class="badge__text"><span>HOLIDAY RENTAL</span><span>BEACH HOUSE</span></div>
  </div>

  <h1 class="title" style="top:406px">Beautiful Family Home For RENT</h1>
  <p class="subtitle" style="top:442px">Carrickalinga - 17 Brindle Street</p>

  <div class="section-rule">INTERIOR VIEW</div>
  <div class="thumbs">
    <div class="thumb" style="background:linear-gradient(160deg,#c9a27a,#7a5438 60%,#3a2a22)" role="img" aria-label="Slow combustion wood heater in stone alcove"></div>
    <div class="thumb" style="background:linear-gradient(160deg,#e8e4dc,#d49a52 55%,#b97a38)" role="img" aria-label="Timber dining table and chairs"></div>
    <div class="thumb" style="background:linear-gradient(160deg,#c8935a,#3f5f9a 45%,#e0665a 75%,#f0c44a)" role="img" aria-label="Bedroom with striped bedspread"></div>
  </div>

  <ul class="features features--front col-a">
    <li>Sleeps 8-10</li>
    <li style="margin-top:6px">4 bedrooms<br>(2 Queen, 1 Double, 2 bunks)</li>
    <li>2 Bathrooms, one with bath,<br>2 toilets</li>
  </ul>
  <ul class="features features--front col-b">
    <li>Open Plan Lounge/Dining<br>Kitchen area</li>
    <li class="fit nowrap">BIR to all bedrooms 2 Bathrooms</li>
    <li style="margin-top:6px">Dining Table for 8 people</li>
  </ul>

  <p class="tagline" style="top:804px">ONE STREET BACK FROM BEACH!</p>

  <div class="contact-rule" style="top:847px"></div>
  <div class="contact" style="height:96px">
    <p class="contact__lead">For further information or to book contact Joan on</p>
    <p class="contact__phone">
      <svg width="20" height="20" viewBox="0 0 20 20" aria-hidden="true"><circle cx="10" cy="10" r="9" fill="none" stroke="#fff" stroke-width="1.6"/><path d="M6.5 5.5 L8.3 5.2 L9.2 7.6 L8.1 8.5 C8.7 9.9 9.9 11.2 11.4 11.9 L12.3 10.8 L14.7 11.7 L14.4 13.5 C10 13.8 6.2 10 6.5 5.5 Z" fill="#fff"/></svg>
      0491 287 306
    </p>
    <p class="contact__email">joanfarrow27@velmarnet.com.au</p>
  </div>
</section>

<section class="leaflet leaflet--back">
  <h2 class="title" style="top:36px">Beautiful Family Home For RENT</h2>
  <p class="subtitle" style="top:73px">Carrickalinga - 17 Brindle Street</p>

  <div class="photo" style="top:120px;height:350px;background:linear-gradient(180deg,#6fa2dc 0%,#a9c8ea 30%,#3f8aa8 34%,#2a6f8a 60%,#8fb7b8 72%,#d9c9a6 82%,#c9b48d 100%)" role="img" aria-label="Photo of the calm sea and sandy beach with headland"></div>
  <svg class="wave" style="top:115px" height="80" viewBox="0 0 452 80" preserveAspectRatio="none" aria-hidden="true">
    <path d="M0,0 L452,0 L452,30 C330,0 200,20 120,40 C70,52 30,50 0,40 Z" fill="#fff"/>
    <path d="M0,40 C40,52 80,50 130,40 C210,22 330,5 452,32 L452,42 C350,18 240,30 150,46 C90,58 40,60 0,52 Z" fill="var(--teal)"/>
    <path d="M180,20 C270,5 370,0 452,20 L452,32 C370,10 270,10 180,20 Z" fill="var(--sand)"/>
  </svg>
  <svg class="wave" style="top:395px" height="85" viewBox="0 0 452 85" preserveAspectRatio="none" aria-hidden="true">
    <path d="M0,40 C120,100 270,80 452,25 L452,85 L0,85 Z" fill="#fff"/>
    <path d="M0,10 C90,75 240,82 452,12 L452,25 C270,80 120,95 0,40 Z" fill="var(--teal)"/>
    <path d="M150,68 C270,58 370,22 452,5 L452,17 C370,38 280,64 150,68 Z" fill="var(--sand)"/>
  </svg>

  <ul class="features features--back col-a">
    <li class="nowrap">Reverse cycle airconditioner</li>
    <li class="nowrap">Slow combustion wood heater</li>
    <li>TV/DVD, CD/Radio</li>
    <li>Kitchen has m/wave, oven,<br>fridge/freezer, dishwasher</li>
  </ul>
  <ul class="features features--back col-b">
    <li>BBQ provided</li>
    <li class="nowrap">Washing Machine and dryer provided</li>
    <li>Timber decking with 2 outside tables<br>and 12 chairs</li>
    <li style="margin-top:-5px">Smoke free zone - No Pets</li>
  </ul>

  <p class="tagline" style="top:620px">ONE STREET BACK FROM BEACH!</p>

  <div class="photo" style="top:651px;height:180px;background:linear-gradient(180deg,#dfe6e6 0%,#6a6a60 30%,#8a6e4c 55%,#6f7378 80%,#9a9a98 100%)" role="img" aria-label="Photo of the timber deck with outdoor tables and teal umbrellas"></div>
  <div class="contact-rule" style="top:840px;height:3px"></div>
  <div class="contact" style="height:94px">
    <p class="contact__lead">For further information or to book contact Joan on</p>
    <p class="contact__phone">
      <svg width="20" height="20" viewBox="0 0 20 20" aria-hidden="true"><circle cx="10" cy="10" r="9" fill="none" stroke="#fff" stroke-width="1.6"/><path d="M6.5 5.5 L8.3 5.2 L9.2 7.6 L8.1 8.5 C8.7 9.9 9.9 11.2 11.4 11.9 L12.3 10.8 L14.7 11.7 L14.4 13.5 C10 13.8 6.2 10 6.5 5.5 Z" fill="#fff"/></svg>
      0491 287 306
    </p>
    <p class="contact__email">joanfarrow27@velmarnet.com.au</p>
  </div>
</section>

</body>
</html>
```